Disability provider requiring digital flyer to promote services

My company works within the Disability sector (QCWP registered provider), currently operating in Sydney, Australia.
I require a digital brochure which lists our services and gives potential customers a quick look into what we do with a single glance.
Undecided whether this digital flyer is to be single or double sided, happy to consult with an experienced designer in this regard.
I prefer minimalist designs (which may be an issue for someone trying to convey information, I'm not sure), and possibly someone who can work with out watercolor logo.
Services include:
-Supported Independent Living
-Specialist Disability Accommodation
-Individualised Living Options Stage 1 & 2
-Home Modifications
-Occupational Therapy
-Support Coordination Levels 1 & 2
-Short Term Accommodation - STA Respite
-Drop In Supports
-Community Access

```html
<!DOCTYPE html>
<html lang="en">
<head>
<meta charset="utf-8">
<title>Sunward Care – Our Services</title>
<link href="https://fonts.googleapis.com/css2?family=Montserrat:wght@400;500;700&display=swap" rel="stylesheet">
<style>
  :root {
    --stage: #3a3a3c;
    --paper: #ffffff;
    --teal: #5bbfbb;
    --teal-deep: #2fbfa0;
    --ink: #4a4a4c;
    --ink-dark: #3a3a3c;
    --blush: #f6d3d8;
    --lilac: #dccbe6;
    --sky: #dcedf6;
    --mist: #f1f4f5;
  }
  * { box-sizing: border-box; margin: 0; padding: 0; }
  html, body {
    width: 1200px; height: 1200px; overflow: hidden;
    background: var(--stage);
    font-family: "Montserrat", sans-serif;
  }
  .flyer {
    position: absolute; left: 255px; top: 111px;
    width: 691px; height: 978px;
    background: var(--paper);
    overflow: hidden;
  }
  .wash {
    position: absolute; inset: 0 0 auto 0; height: 470px;
    background:
      radial-gradient(ellipse 260px 200px at 40px 40px, var(--blush), transparent 70%),
      radial-gradient(ellipse 160px 120px at 360px 0px, var(--sky), transparent 70%),
      radial-gradient(ellipse 200px 230px at 680px 70px, var(--lilac), transparent 70%),
      radial-gradient(ellipse 120px 180px at 0px 300px, var(--lilac), transparent 70%),
      var(--paper);
    opacity: .9;
  }
  .brand-art {
    position: absolute; left: 170px; top: 42px;
    width: 350px; height: 219px;
    border-radius: 6px;
    background: linear-gradient(90deg, #e0509c 0%, #c77fd0 40%, #f6b54a 70%, #f4c95a 100%);
    opacity: .75;
  }
  .brand-name {
    position: absolute; left: 0; right: 0; top: 282px;
    text-align: center;
    font-weight: 500; font-size: 56px; letter-spacing: 2px;
    color: var(--ink-dark); line-height: 1.1;
  }
  .services-band {
    position: absolute; left: 0; right: 0; top: 466px; bottom: 0;
    background: linear-gradient(var(--mist), var(--paper) 200px);
    border-top: 5px solid var(--teal);
  }
  .services-title {
    position: absolute; left: 217px; top: 442px;
    width: 259px; height: 48px; border-radius: 24px;
    background: var(--teal); color: #fff;
    font-weight: 700; font-size: 30px;
    display: flex; align-items: center; justify-content: center;
  }
  .service {
    position: absolute;
    display: flex; align-items: center; gap: 17px;
    font-weight: 500; font-size: 21px; line-height: 25px;
    color: var(--ink);
  }
  .service svg { width: 38px; height: 38px; flex: none; }
  .col-left { left: 54px; }
  .col-right { left: 353px; }
  .grass {
    position: absolute; left: 0; right: 0; bottom: 0; height: 96px;
    background: linear-gradient(180deg, rgba(91,191,187,0) 0%, var(--teal) 35%, var(--teal-deep) 100%);
  }
  .website {
    position: absolute; left: 0; right: 0; bottom: 8px;
    text-align: center; color: #fff;
    font-weight: 400; font-size: 22px; letter-spacing: .5px;
  }
</style>
</head>
<body>
<svg width="0" height="0" style="position:absolute">
  <defs>
    <symbol id="tick" viewBox="0 0 40 40">
      <path d="M27 10 A16 16 0 1 0 34 22" fill="none" stroke="#5bbfbb" stroke-width="3"/>
      <path d="M10 20 L18 30 L37 5 L19 22 Z" fill="#5bbfbb"/>
    </symbol>
  </defs>
</svg>

<main class="flyer">
  <div class="wash"></div>
  <div class="brand-art" role="img" aria-label="Watercolour illustration of a tree with a swing, birds, and a person in a wheelchair high-fiving a standing companion"></div>
  <h1 class="brand-name">SUNWARD CARE</h1>

  <section class="services-band"></section>
  <h2 class="services-title">Our Services</h2>

  <div class="service col-left" style="top:546px"><svg><use href="#tick"/></svg><span>Supported<br>Independent Living</span></div>
  <div class="service col-left" style="top:610px"><svg><use href="#tick"/></svg><span>Specialist Disability<br>Accommodation</span></div>
  <div class="service col-left" style="top:674px"><svg><use href="#tick"/></svg><span>Individualised Living<br>Options Stage 1 &amp; 2</span></div>
  <div class="service col-left" style="top:738px"><svg><use href="#tick"/></svg><span>Home<br>Modifications</span></div>
  <div class="service col-left" style="top:804px"><svg><use href="#tick"/></svg><span>Community<br>Access</span></div>

  <div class="service col-right" style="top:546px"><svg><use href="#tick"/></svg><span>Occupational<br>Therapy</span></div>
  <div class="service col-right" style="top:610px"><svg><use href="#tick"/></svg><span>Support Coordination<br>Levels 1 &amp; 2</span></div>
  <div class="service col-right" style="top:674px"><svg><use href="#tick"/></svg><span>Short Term<br>Accommodation<br>STA Respite</span></div>
  <div class="service col-right" style="top:763px"><svg><use href="#tick"/></svg><span>Drop<br>In Supports</span></div>

  <div class="grass" role="img" aria-label="Teal watercolour grass border along the bottom edge"></div>
  <p class="website">www.website.com</p>
</main>
</body>
</html>
```